Label for Skincare Brand

"Fernleigh Vale Organics" - organic skincare brand
I need a label designed for my organic skincare brand. I have attached pics of brands I like, to give you an idea of style. I would like something minimal although some colour might work. Colours I like are pale blush pink and aqua. I would like a clean, minimalistic modern yet elegant label. Please look at the samples because they demonstrate the style I look for in a label. It is okay to add a graphical element into the design as long as it enhances or add value to the design.
We do not have a logo yet, so I'd appreciate if you could create a simple type logo for Fernleigh Vale Organics similar to the examples attached.
Please can you do two different sizes: one cream jar and one serum bottle. Both will contain the same information.
___________________________________________________
1. Cream Jar (label size 42 x 190 mm) (clear glass with aluminium lid)
2. Serum Bottle (label size 50 x 110 mm) (clear glass with black pump)
FRONT SIDE:
Fernleigh Vale Organics
Nine Moons
Ultimate Anti-Aging Cream
For Dry & Mature Skin
Organic & Palm Oil-Free
100 ml.
BACK SIDE:
Nine Moons Ultimate Anti-Aging Cream
An effective Day Cream that harnesses the best of science to target the signs of aging. The main active ingredient is R58, a patented noncomedogenic lipid complex, carefully engineered from botanically-sourced lipids. It is composed of a variety of lipid types which are carefully combined in the same ratio as those found on healthy young skin of an average 22 year old.
Directions:
Apply to clean skin morning and night.
Ingredients:
Aloe Vera Leaf Juice, Cocos Nucifera Oil, Butyrospermum Parkii Butter, Jojoba Oil/Macadamia Seed Oil Esters (and) Squalene (and) Phytosteryl Macadamiate (and) Phytosterols, Potassium Olivoyl Hydrolyzed Oat Protein (and) Cetearyl Alcohol (and) Glyceryl Oleate (and) Glyceryl Stearat, Benzyl Alcohol, Dehydroacetic Acid.
Fernleigh Vale Organics
6/3 Kelmora Street North, Wahroonga, NSW 2076
www.fernleighvaleorganics.com.au
Any questions, please just ask away. Thank you.

```html
<!DOCTYPE html>
<html lang="en">
<head>
<meta charset="utf-8">
<title>Fernleigh Vale Organics – Nine Moons Cream Jar Label</title>
<link href="https://fonts.googleapis.com/css2?family=Jost:wght@500;600&family=Space+Mono&family=Crimson+Pro:ital,wght@0,400;0,600;1,400&display=swap" rel="stylesheet">
<style>
  :root {
    --backdrop: #ececec;
    --label: #ffffff;
    --ink: #141414;
    --ink-soft: #4a4a4a;
    --blush: #f6cdb5;
  }
  * { margin: 0; padding: 0; box-sizing: border-box; }
  html, body {
    width: 1200px;
    height: 1200px;
    overflow: hidden;
    background: var(--backdrop);
  }
  .jar-label {
    position: absolute;
    left: 30px;
    top: 474px;
    width: 1140px;
    height: 252px;
    background: var(--label);
    overflow: hidden;
    color: var(--ink);
    box-shadow: 0 2px 10px rgba(0,0,0,0.06);
  }
  .accent-circle {
    position: absolute;
    left: 236px;
    top: 18px;
    width: 216px;
    height: 216px;
    border-radius: 50%;
    background: var(--blush);
  }
  .front-panel {
    position: absolute;
    left: 42px;
    top: 36px;
  }
  .brand-name {
    font-family: "Jost", sans-serif;
    font-weight: 600;
    font-size: 11px;
    letter-spacing: 0.14em;
    text-transform: uppercase;
    padding-bottom: 5px;
    border-bottom: 1.5px solid var(--ink);
    display: inline-block;
  }
  .product-name {
    position: relative;
    margin-top: 12px;
    font-family: "Jost", sans-serif;
    font-weight: 600;
    font-size: 46px;
    line-height: 1;
    letter-spacing: 0.07em;
    white-space: nowrap;
  }
  .product-number {
    position: absolute;
    top: -8px;
    right: -24px;
    font-size: 12px;
    font-weight: 500;
    letter-spacing: 0.05em;
  }
  .product-type {
    margin-top: 16px;
    font-family: "Space Mono", monospace;
    font-size: 13px;
    line-height: 1.35;
  }
  .product-claim {
    margin-top: 12px;
    font-family: "Crimson Pro", serif;
    font-style: italic;
    font-size: 12px;
    letter-spacing: 0.04em;
  }
  .net-volume {
    margin-top: 10px;
    font-family: "Crimson Pro", serif;
    font-size: 12px;
    letter-spacing: 0.04em;
  }
  .back-column {
    position: absolute;
    top: 38px;
    width: 222px;
    font-family: "Crimson Pro", serif;
    font-size: 10px;
    line-height: 1.3;
    color: var(--ink-soft);
  }
  .back-column h2,
  .back-column h3 {
    font-family: "Crimson Pro", serif;
    font-weight: 600;
    color: var(--ink);
  }
  .back-column h2 { font-size: 13px; line-height: 1.15; margin-bottom: 6px; }
  .back-column h3 { font-size: 11px; margin-top: 8px; margin-bottom: 2px; }
  .back-column h3:first-child { margin-top: 0; }
  .column-story { left: 412px; }
  .column-usage { left: 664px; }
  .column-maker { left: 912px; }
  .maker-details { margin-top: 86px; }
  .maker-details .maker-name {
    font-family: "Jost", sans-serif;
    font-weight: 600;
    font-size: 10px;
    letter-spacing: 0.14em;
    text-transform: uppercase;
    color: var(--ink);
    margin-bottom: 4px;
  }
</style>
</head>
<body>
  <section class="jar-label">
    <div class="accent-circle"></div>

    <div class="front-panel">
      <div class="brand-name">Fernleigh Vale Organics</div>
      <h1 class="product-name">Nine Moons<span class="product-number">9</span></h1>
      <p class="product-type">Ultimate Anti-Aging Cream<br>For Dry &amp; Mature Skin</p>
      <p class="product-claim">Organic &amp; Palm Oil-Free</p>
      <p class="net-volume">100 ml.</p>
    </div>

    <div class="back-column column-story">
      <h2>Nine Moons<br>Ultimate Anti-Aging Cream</h2>
      <p>An effective Day Cream that harnesses the best of science to target the signs of aging. The main active ingredient is R58, a patented noncomedogenic lipid complex, carefully engineered from botanically-sourced lipids. It is composed of a variety of lipid types which are carefully combined in the same ratio as those found on healthy young skin of an average 22 year old.</p>
    </div>

    <div class="back-column column-usage">
      <h3>Directions:</h3>
      <p>Apply to clean skin morning and night.</p>
      <h3>Ingredients:</h3>
      <p>Aloe Vera Leaf Juice, Cocos Nucifera Oil, Butyrospermum Parkii Butter, Jojoba Oil/Macadamia Seed Oil Esters (and) Squalene (and) Phytosteryl Macadamiate (and) Phytosterols, Potassium Olivoyl Hydrolyzed Oat Protein (and) Cetearyl Alcohol (and) Glyceryl Oleate (and) Glyceryl Stearat, Benzyl Alcohol, Dehydroacetic Acid.</p>
    </div>

    <div class="back-column column-maker">
      <div class="maker-details">
        <p class="maker-name">Fernleigh Vale Organics</p>
        <p>6/3 Kelmora Street North, Wahroonga, NSW 2076</p>
        <p>www.fernleighvaleorganics.com.au</p>
      </div>
    </div>
  </section>
</body>
</html>
```